Business card and Stationery for data intelligence company

We need a new design for our business cards and stationery (Business Letter templates and a Quote example on Word, but it MUST work on Google Doc as well).

We are a software company based in Ireland and UK. Our product is "Kovar", data intelligence platform with beautiful visualizations, graph capabilities (things are interconnected), powerful, flexible, it can manage Big Data and Streaming information. It's modern and relatively open source.
Our company will provide data intelligence for law enforcements, pharmaceuticals, and similar high end customers.

We'll launch a new website soon. At the moment it's http://www.kovar-analytics.example if you want to take a look. This is our youtube channel in case you need it to understand what Kovar is: https://www.youtube.com/c/kovaranalyticschannel

We changed the logo so please use the logo I attach here.

We'd like the output to be cool and modern but elegant and "business" at the same time. It should inspire simple sophistication, "unity" "intent" "purpose" yet subtly very advanced and innovative.

The name "Kovar" does NOT refer to sirens (mithological creatures) as well as the warning devices. It means Kinetic Object Vector Analysis Reactor. Please use our logo's colors and if you want to something like the "graph" image.

```html
<!DOCTYPE html>
<html lang="en">
<head>
<meta charset="utf-8">
<title>Kovar – Stationery and Presentation Set</title>
<link href="https://fonts.googleapis.com/css2?family=Open+Sans:ital,wght@0,400;0,600;0,700;1,400&display=swap" rel="stylesheet">
<style>
:root{
  --stage:#a7a7a7;
  --paper:#f4f3f1;
  --white:#fbfbfb;
  --orange:#f5a93a;
  --orange-soft:#f8c172;
  --grey:#8c8c8c;
  --grey-light:#c9c9c9;
  --ink:#3a3a3a;
  --photo:#3d3d3d;
}
*{margin:0;padding:0;box-sizing:border-box}
html,body{width:1200px;height:386px;overflow:hidden;background:var(--stage)}
body{position:relative;font-family:"Open Sans",Arial,sans-serif;color:var(--ink)}
.sheet{position:absolute;background:var(--paper);overflow:hidden}
.edge-bar{position:absolute;left:0;right:0;bottom:0;height:3px;background:linear-gradient(90deg,var(--orange) 0 82%,var(--grey-light) 82% 100%)}
.brand{display:flex;align-items:center;gap:3px;color:var(--orange);font-weight:600;letter-spacing:.08em;line-height:1}
.brand-dot{border-radius:50%;background:var(--orange);flex:none}

/* letterhead */
.letterhead{top:16px;width:249px;height:352px}
.letterhead--first{left:30px}
.letterhead--follow{left:286px}
.letterhead .brand{position:absolute;left:22px;top:29px;font-size:11px}
.letterhead .brand-dot{width:9px;height:9px}
.sender-address{position:absolute;right:62px;top:20px;font-size:4.4px;line-height:5.4px;text-align:right}
.sender-contacts{position:absolute;left:192px;top:18px;padding-left:6px;border-left:.5px solid var(--grey);font-size:4.2px;line-height:5.8px;list-style:none}
.sender-contacts li{display:flex;align-items:center;gap:2px}
.ico{width:4px;height:4px;flex:none}
.letter-body{position:absolute;left:24px;top:114px;width:204px;font-size:4.1px;line-height:6.2px}
.letter-salutation{font-size:6.2px;margin-bottom:10px}
.letter-body p{margin-bottom:6px}
.sign-off{position:absolute;left:24px;top:252px;font-size:4.2px;line-height:6px}
.signature{display:block;width:32px;height:10px;margin:6px 0 4px 8px;background:linear-gradient(90deg,transparent,#6d6d6d 30%,#6d6d6d 70%,transparent);opacity:.35;border-radius:5px}
.sign-off .signer{padding-left:10px}
.letter-web{position:absolute;left:0;right:0;bottom:14px;text-align:center;font-size:4.4px;letter-spacing:.25em}

/* business card */
.card{top:152px;width:110px;height:62px}
.card--front{left:578px;background:var(--white)}
.card--front .brand{position:absolute;right:10px;top:9px;font-size:7px}
.card--front .brand-dot{width:6px;height:6px}
.card-name{position:absolute;left:8px;top:26px;font-size:4.6px;color:var(--orange);font-weight:600;letter-spacing:.05em}
.card-role{position:absolute;left:8px;top:32px;font-size:3px;color:var(--grey)}
.card-contacts{position:absolute;left:8px;top:37px;list-style:none;font-size:3px;line-height:4.2px}
.card-contacts li{display:flex;gap:2px;align-items:center}
.card-contacts .ico{width:2.6px;height:2.6px}
.card-address{position:absolute;left:48px;top:46px;padding-left:3px;border-left:.4px solid var(--grey);font-size:3px;line-height:4.2px}
.card--front .edge-bar{height:2px;right:28px;background:var(--orange)}
.card--back{left:704px;background:var(--orange)}
.card--back .brand{position:absolute;right:8px;top:38px;color:#fff;font-size:10px}
.card--back .brand-dot{width:7px;height:7px;background:#fff}
.card-back-web{position:absolute;right:8px;top:51px;color:#fff;font-size:3px;letter-spacing:.3em}

/* envelope */
.envelope{left:550px;top:240px;width:282px;height:128px;background:var(--white)}
.envelope .brand{position:absolute;left:15px;top:21px;font-size:11px}
.envelope .brand-dot{width:9px;height:9px}
.envelope-return{position:absolute;left:16px;top:42px;font-size:4.6px;line-height:5.6px;font-style:italic}
.envelope .edge-bar{background:linear-gradient(90deg,var(--orange) 0 84%,var(--grey-light) 84% 100%)}

/* slides */
.slide{position:absolute;width:148px;height:111px;background:linear-gradient(180deg,#f7f7f7 0%,#e6e6e6 60%,#cfcfcf 100%);overflow:hidden}
.slide .edge-bar{height:2px;background:linear-gradient(90deg,var(--orange) 0 76%,transparent 76%)}
.col-a{left:860px}.col-b{left:1018px}
.row-1{top:19px}.row-2{top:138px}.row-3{top:259px}
.slide-head{position:absolute;left:8px;top:6px;right:8px;height:17px;border-bottom:.5px solid var(--grey-light)}
.slide-title{font-size:6.6px;color:var(--orange);font-weight:600}
.slide-sub{font-size:3.4px;color:var(--grey)}
.slide-mark{position:absolute;right:0;top:1px;width:7px;height:7px;border-radius:50%;background:var(--orange)}
.micro{font-size:2.6px;line-height:3.6px;color:#555}
.micro-label{font-size:3px;color:var(--orange);font-weight:600;margin-bottom:1px}

.slide--cover .brand{position:absolute;left:22px;top:32px;font-size:19px}
.slide--cover .brand-dot{width:15px;height:15px}
.cover-title{position:absolute;left:0;right:0;top:74px;text-align:center;font-size:8.4px;font-weight:700;color:#111}
.cover-text{position:absolute;left:30px;right:30px;top:85px;text-align:center}

.photo-row{position:absolute;left:13px;right:13px;top:30px;display:flex;justify-content:space-between}
.photo-cell{width:27px}
.photo{height:27px;background:var(--photo);border:1px solid #fff;display:flex;align-items:center;justify-content:center;color:#ddd;font-size:3.2px}
.photo-cell .micro-label{margin-top:5px}

.two-col{position:absolute;left:8px;right:8px;top:27px;display:grid;grid-template-columns:1fr 1fr;gap:4px 8px}
.two-col .micro-label{margin-top:2px}

.bar-chart{position:absolute;left:18px;top:28px;width:62px;height:62px}
.chart-note{position:absolute;left:90px;top:30px;width:50px}
.chart-foot{position:absolute;left:8px;right:8px;top:92px}

.pie-text{position:absolute;left:8px;top:32px;width:66px}
.pie{position:absolute;left:86px;top:34px;width:36px;height:36px}
.pie-legend{position:absolute;left:86px;top:76px;list-style:none}
.pie-legend li{display:flex;align-items:center;gap:2px}
.swatch{width:3px;height:3px;flex:none}

.slide--thanks{background:var(--orange)}
.thanks{position:absolute;left:0;right:0;top:38px;text-align:center;color:#fff;line-height:1}
.thanks-main{font-size:18px;font-weight:600;letter-spacing:.04em}
.thanks-sub{font-size:9.5px;letter-spacing:.16em;margin-top:2px}
</style>
</head>
<body>

<!-- Letterhead: first page -->
<section class="sheet letterhead letterhead--first" aria-label="Letterhead first page">
  <div class="brand"><span class="brand-dot"></span>KOVAR</div>
  <address class="sender-address" style="font-style:normal">41 Harbour Row<br>Galway<br>H91 K2X4</address>
  <ul class="sender-contacts">
    <li><svg class="ico" viewBox="0 0 10 10"><path d="M2 1h2l1 2-1.3 1a6 6 0 0 0 2.3 2.3L7 5l2 1v2c0 .6-.5 1-1 1A8 8 0 0 1 1 2c0-.6.4-1 1-1z" fill="var(--orange)"/></svg>091 555 0142</li>
    <li><svg class="ico" viewBox="0 0 10 10"><rect x="2.5" y="1" width="5" height="8" rx="1" fill="var(--orange)"/></svg>091 555 0178</li>
    <li><svg class="ico" viewBox="0 0 10 10"><rect x="1" y="4" width="8" height="5" fill="var(--orange)"/><rect x="3" y="1" width="4" height="3" fill="var(--orange)"/></svg>091 555 0193</li>
    <li><svg class="ico" viewBox="0 0 10 10"><rect x="1" y="2" width="8" height="6" fill="var(--orange)"/><path d="M1 2l4 3 4-3" stroke="#fff" fill="none" stroke-width=".8"/></svg>name@kovar.example</li>
  </ul>
  <div class="letter-body">
    <p class="letter-salutation">Dear Mr. Doyle,</p>
    <p>Thank you for your time last week and for the clear overview of your current data workflow. As promised, this letter sets out how our platform can bring your separate sources into one connected view, with streaming updates, graph links between records and fast visual analysis that your teams can share across every office with ease.</p>
    <p>Our proposal covers setup, secure hosting, onboarding for your analysts and a period of close support while the first projects go live. Each stage has a fixed scope and a named lead on our side, so progress is simple to follow and every question has a quick and direct answer.</p>
    <p>We would also like to run a short pilot on one of your live cases. This lets your staff test the tools on real work, measure the time saved and judge the results before any wider rollout begins. We are happy to adapt the plan to suit your schedule.</p>
    <p>Please find the full quote enclosed. If anything needs more detail, we will gladly arrange a call at a time that suits you.</p>
  </div>
  <div class="sign-off">
    <p>Sincerely,</p>
    <span class="signature" role="img" aria-label="Handwritten signature"></span>
    <p class="signer">Ewan Doyle<br>CEO/ Founder</p>
  </div>
  <p class="letter-web">www.kovar-analytics.example</p>
  <div class="edge-bar"></div>
</section>

<!-- Letterhead: follow-on page -->
<section class="sheet letterhead letterhead--follow" aria-label="Letterhead follow-on page">
  <div class="edge-bar"></div>
</section>

<!-- Business card front -->
<section class="sheet card card--front" aria-label="Business card front">
  <div class="brand"><span class="brand-dot"></span>KOVAR</div>
  <p class="card-name">EWAN DOYLE</p>
  <p class="card-role">CEO/ Founder</p>
  <ul class="card-contacts">
    <li><svg class="ico" viewBox="0 0 10 10"><circle cx="5" cy="5" r="4" fill="var(--orange)"/></svg>091 555 0142</li>
    <li><svg class="ico" viewBox="0 0 10 10"><circle cx="5" cy="5" r="4" fill="var(--orange)"/></svg>091 555 0178</li>
    <li><svg class="ico" viewBox="0 0 10 10"><circle cx="5" cy="5" r="4" fill="var(--orange)"/></svg>091 555 0193</li>
    <li><svg class="ico" viewBox="0 0 10 10"><circle cx="5" cy="5" r="4" fill="var(--orange)"/></svg>name@kovar.example</li>
    <li><svg class="ico" viewBox="0 0 10 10"><circle cx="5" cy="5" r="4" fill="var(--orange)"/></svg>www.kovar.example</li>
  </ul>
  <p class="card-address">41 Harbour Row<br>Galway, H91 K2X4</p>
  <div class="edge-bar"></div>
</section>

<!-- Business card back -->
<section class="sheet card card--back" aria-label="Business card back">
  <div class="brand"><span class="brand-dot"></span>KOVAR</div>
  <p class="card-back-web">www.kovar.example</p>
</section>

<!-- Envelope -->
<section class="sheet envelope" aria-label="Envelope">
  <div class="brand"><span class="brand-dot"></span>KOVAR</div>
  <p class="envelope-return">41 Harbour Row, Galway<br>H91 K2X4</p>
  <div class="edge-bar"></div>
</section>

<!-- Slide: cover -->
<section class="slide slide--cover col-a row-1" aria-label="Presentation cover slide">
  <div class="brand"><span class="brand-dot"></span>KOVAR</div>
  <h1 class="cover-title">PRESENTATION TITLE</h1>
  <p class="cover-text micro">A short line of supporting text that sets out the purpose of this talk and the main points that the audience will see over the next few slides.</p>
  <div class="edge-bar"></div>
</section>

<!-- Slide: team photos -->
<section class="slide col-b row-1" aria-label="Team slide">
  <header class="slide-head"><p class="slide-title">Heading Here</p><p class="slide-sub">Sub Heading</p><span class="slide-mark"></span></header>
  <div class="photo-row">
    <div class="photo-cell"><div class="photo" role="img" aria-label="Team member photo">Photo</div><p class="micro-label">Team member</p><p class="micro">Role title here in brief words.</p></div>
    <div class="photo-cell"><div class="photo" role="img" aria-label="Team member photo">Photo</div><p class="micro-label">Team member</p><p class="micro">Role title here in brief words.</p></div>
    <div class="photo-cell"><div class="photo" role="img" aria-label="Team member photo">Photo</div><p class="micro-label">Team member</p><p class="micro">Role title here in brief words.</p></div>
    <div class="photo-cell"><div class="photo" role="img" aria-label="Team member photo">Photo</div><p class="micro-label">Team member</p><p class="micro">Role title here in brief words.</p></div>
  </div>
  <div class="edge-bar"></div>
</section>

<!-- Slide: grouped text -->
<section class="slide col-a row-2" aria-label="Grouped text slide">
  <header class="slide-head"><p class="slide-title">Heading Here</p><p class="slide-sub">Sub Heading</p><span class="slide-mark"></span></header>
  <div class="two-col">
    <div><p class="micro-label">Group1</p><p class="micro">Short text on the first topic with a few key facts and one clear idea for the team.</p></div>
    <div><p class="micro-label">Group4</p><p class="micro">Short text on the fourth topic with a few key facts and one clear idea for the team.</p></div>
    <div><p class="micro-label">Group2</p><p class="micro">Short text on the second topic with a few key facts and one clear idea.</p></div>
    <div><p class="micro-label">Group5</p><p class="micro">Short text on the fifth topic with a few key facts and one clear idea.</p></div>
    <div><p class="micro-label">Group3</p><p class="micro">Short text on the third topic with a few key facts and one clear idea.</p></div>
  </div>
  <div class="edge-bar"></div>
</section>

<!-- Slide: bar chart -->
<section class="slide col-b row-2" aria-label="Bar chart slide">
  <header class="slide-head"><p class="slide-title">Heading Here</p><p class="slide-sub">Sub Heading</p><span class="slide-mark"></span></header>
  <svg class="bar-chart" viewBox="0 0 62 62" aria-label="Bar chart">
    <g stroke="var(--grey-light)" stroke-width=".3"><line x1="0" y1="10" x2="62" y2="10"/><line x1="0" y1="25" x2="62" y2="25"/><line x1="0" y1="40" x2="62" y2="40"/><line x1="0" y1="55" x2="62" y2="55"/></g>
    <rect x="6" y="6" width="9" height="49" fill="var(--orange)"/>
    <rect x="19" y="16" width="9" height="39" fill="var(--orange)"/>
    <rect x="32" y="26" width="9" height="29" fill="var(--orange)"/>
    <rect x="45" y="18" width="9" height="37" fill="var(--orange)"/>
  </svg>
  <div class="chart-note micro"><p>Key result for this period, shown in brief.</p><p style="margin-top:4px">Second note on the growth trend.</p><p style="margin-top:4px">Third note on what comes next.</p></div>
  <p class="chart-foot micro">A short summary of what the chart shows and why the numbers matter for the plan ahead.</p>
  <div class="edge-bar"></div>
</section>

<!-- Slide: pie chart -->
<section class="slide col-a row-3" aria-label="Pie chart slide">
  <header class="slide-head"><p class="slide-title">Heading Here</p><p class="slide-sub">Sub Heading</p><span class="slide-mark"></span></header>
  <div class="pie-text micro"><p>A short block of text that explains the share of each part in the chart and what the main slice means for the results of this quarter.</p><p style="margin-top:4px">A second note on the smaller slices and how they may change next time.</p></div>
  <svg class="pie" viewBox="0 0 32 32" aria-label="Pie chart">
    <path d="M16 16L16 1A15 15 0 1 1 7.18 28.14Z" fill="var(--orange)"/>
    <path d="M16 16L7.18 28.14A15 15 0 0 1 1.73 11.36Z" fill="#7a7a7a"/>
    <path d="M16 16L1.73 11.36A15 15 0 0 1 16 1Z" fill="#a9a9a9"/>
  </svg>
  <ul class="pie-legend micro">
    <li><span class="swatch" style="background:var(--orange)"></span>Main share 60%</li>
    <li><span class="swatch" style="background:#7a7a7a"></span>Second share 20%</li>
  </ul>
  <div class="edge-bar"></div>
</section>

<!-- Slide: closing -->
<section class="slide slide--thanks col-b row-3" aria-label="Closing slide">
  <div class="thanks"><p class="thanks-main">THANKS</p><p class="thanks-sub">FOR COMING</p></div>
</section>

</body>
</html>
```